I am looking for a modern, clean and neat design for a reflexology and well being business. The business name is Mira Tellus (this is an old Latin word for wellbeing). The colours I would like are purple, white and grey. I am open to suggestions for pictures such as healing or working hands, a pair of feet, images that represent my business that you may think of....... or maybe you think no images at all would be best? My tag line is: "Relax, Renew, Revive" or "Find you balance......... Relax, Renew, Revive" I can decide which I want so I would like to see what both would look like. I would like space on the back to write the client's appointment date and time (more than once)

```html
<!DOCTYPE html>
<html lang="en">
<head>
<meta charset="utf-8">
<title>Mira Tellus – Business Card</title>
<link rel="stylesheet" href="https://fonts.googleapis.com/css2?family=Lato:wght@400;700;900&display=swap">
<style>
  :root {
    --purple: #77308f;
    --purple-dark: #5a2170;
    --charcoal: #333234;
    --band-grey: #58575a;
    --strip-grey: #ececec;
    --ink: #2e2d2f;
    --white: #ffffff;
    --backdrop: #29292b;
  }
  * { box-sizing: border-box; margin: 0; padding: 0; }
  html, body {
    width: 1200px; height: 971px; overflow: hidden;
    background: var(--backdrop);
    font-family: "Lato", sans-serif;
  }
  .card {
    position: absolute;
    left: 232px;
    width: 735px; height: 420px;
    background: var(--white);
    overflow: hidden;
    box-shadow: 0 10px 30px rgba(0,0,0,.45);
  }
  .card--back { top: 48px; }
  .card--front { top: 503px; }
  .card__shapes { position: absolute; inset: 0; }

  .brand {
    position: absolute;
    display: flex; align-items: center; gap: 14px;
    white-space: nowrap;
  }
  .brand__mark { width: 34px; height: 34px; background: var(--purple); border-radius: 6px; flex: none; }
  .brand__name { font-size: 36px; font-weight: 700; letter-spacing: .5px; }
  .card--back .brand { left: 190px; top: 189px; }
  .card--back .brand__name { color: var(--white); }
  .card--front .brand { left: 62px; top: 112px; }
  .card--front .brand__name { color: var(--ink); }

  .appointment {
    position: absolute; left: 568px; top: 174px;
    color: var(--purple); font-weight: 700; font-size: 14px; line-height: 1.6;
    white-space: nowrap;
  }
  .appointment__row { display: flex; align-items: flex-end; gap: 8px; }
  .appointment__line { display: inline-block; width: 100px; border-bottom: 1px solid var(--purple); margin-bottom: 5px; }

  .person { position: absolute; right: 56px; top: 78px; text-align: right; white-space: nowrap; }
  .person__name { font-size: 28px; color: var(--ink); letter-spacing: .5px; }
  .person__name strong { font-weight: 900; }
  .person__role { font-size: 14px; color: var(--purple); letter-spacing: 1px; margin-top: -2px; }

  .contact {
    position: absolute; top: 268px;
    color: var(--white); font-size: 16px; line-height: 1.3; letter-spacing: .3px;
    white-space: nowrap;
  }
  .contact--phone { left: 332px; letter-spacing: 1.2px; }
  .contact--web { left: 512px; }

  .tagline {
    position: absolute; left: 300px; top: 345px;
    color: var(--purple); font-weight: 700; font-size: 28px;
    white-space: nowrap;
  }
</style>
</head>
<body>

<section class="card card--back" aria-label="Card back">
  <svg class="card__shapes" viewBox="0 0 735 420" aria-hidden="true">
    <rect class="band" x="0" y="150" width="505" height="120" fill="#58575a"/>
    <path d="M505 150 L540 210 L505 270 Z" fill="#58575a"/>
    <rect class="logo-panel" x="150" y="108" width="340" height="204" rx="26" fill="#333234"/>
  </svg>
  <div class="brand">
    <span class="brand__mark"></span>
    <span class="brand__name">Mira Tellus</span>
  </div>
  <div class="appointment">
    <div>Client's appointment:</div>
    <div class="appointment__row">Date: <span class="appointment__line"></span></div>
    <div class="appointment__row">Time: <span class="appointment__line"></span></div>
  </div>
</section>

<section class="card card--front" aria-label="Card front">
  <svg class="card__shapes" viewBox="0 0 735 420" aria-hidden="true">
    <rect class="contact-band" x="0" y="230" width="735" height="92" fill="#333234"/>
    <rect class="tagline-strip" x="0" y="322" width="735" height="98" fill="#ececec"/>
    <path class="ribbon-fold" d="M58 205 L74 190 L74 230 Z" fill="#5a2170"/>
    <path class="ribbon-fold" d="M236 205 L220 190 L220 230 Z" fill="#5a2170"/>
    <rect class="ribbon" x="74" y="190" width="146" height="160" rx="16" fill="#77308f"/>
    <path class="icon-tab" d="M380 230 h52 v24 q0 8 -8 8 h-36 q-8 0 -8 -8 Z" fill="#77308f"/>
    <g class="icon-phone" fill="#fff">
      <path d="M394 240 q12 -6 24 0 v4 h-5 v-2 q-7 -2 -14 0 v2 h-5 Z"/>
      <rect x="397" y="245" width="18" height="10" rx="2"/>
    </g>
    <path class="icon-tab" d="M586 230 h52 v24 q0 8 -8 8 h-36 q-8 0 -8 -8 Z" fill="#77308f"/>
    <g class="icon-monitor" fill="none" stroke="#fff" stroke-width="2">
      <rect x="602" y="237" width="20" height="13" rx="1"/>
      <path d="M612 250 v4 M606 255 h12"/>
    </g>
  </svg>
  <div class="brand">
    <span class="brand__mark"></span>
    <span class="brand__name">Mira Tellus</span>
  </div>
  <div class="person">
    <div class="person__name"><strong>OWEN</strong> HARTLEY</div>
    <div class="person__role">DESIGNATION</div>
  </div>
  <div class="contact contact--phone">
    <div>000 . 1234 . 5678</div>
    <div>000 . 1234 . 5679</div>
  </div>
  <div class="contact contact--web">
    <div>hello@miratellus-care.com</div>
    <div>www.miratellus-care.com</div>
  </div>
  <div class="tagline">Relax, Renew, Revive</div>
</section>

</body>
</html>
```